Harbourline construction company Business card design

I need a business card design for my company. I have a logo but dont have business cards with our logo..

www.harbourlineconstructco.com.au

The logo is on the website

I need the same details as this design I have attached. we have changed the logo and colours. just like the website

Industry/Entity Type

Building

```html
<!DOCTYPE html>
<html lang="en">
<head>
<meta charset="utf-8">
<title>Harbourline Construction – Business Card</title>
<link rel="stylesheet" href="https://fonts.googleapis.com/css2?family=Lato:wght@400;700&family=Cinzel:wght@400&display=swap">
<style>
  :root {
    --backdrop: #2b2b2c;
    --card-grey: #c3c4c6;
    --card-white: #ffffff;
    --brand-blue: #1b8ac7;
    --ink: #1d1d1f;
    --rule: #3a3a3c;
    --soft-rule: #b9babc;
    --strip-grey: #bcbdbf;
  }
  * { box-sizing: border-box; margin: 0; padding: 0; }
  html, body {
    width: 1200px; height: 800px; overflow: hidden;
    background: var(--backdrop);
    font-family: "Lato", Arial, sans-serif;
    color: var(--ink);
  }
  .card {
    position: absolute;
    top: 242px;
    width: 520px; height: 316px;
    overflow: hidden;
  }
  /* Front */
  .card-front { left: 50px; background: var(--card-grey); }
  .card-front .rule {
    position: absolute; height: 1.5px; background: var(--rule);
  }
  .card-front .rule-top { top: 58px; left: 300px; width: 200px; }
  .card-front .rule-bottom { top: 262px; left: 22px; width: 200px; }
  .brand {
    display: flex; align-items: center; gap: 14px;
  }
  .brand-square { background: var(--brand-blue); flex: none; }
  .brand-name {
    color: var(--brand-blue);
    font-weight: 400;
    text-transform: uppercase;
    line-height: 1.05;
  }
  .card-front .brand {
    position: absolute; left: 0; right: 0; top: 92px; justify-content: center;
  }
  .card-front .brand-square { width: 34px; height: 34px; }
  .card-front .brand-name { font-size: 30px; letter-spacing: 4px; }
  .tagline { color: var(--ink); line-height: 1.2; }
  .card-front .tagline {
    position: absolute; left: 0; right: 0; top: 188px;
    text-align: center; font-size: 16px;
  }
  /* Back */
  .card-back { left: 630px; background: var(--card-white); }
  .card-back .brand-block { position: absolute; left: 20px; top: 58px; width: 222px; }
  .card-back .brand { gap: 10px; }
  .card-back .brand-square { width: 22px; height: 22px; }
  .card-back .brand-name { font-size: 19px; letter-spacing: 1.5px; }
  .card-back .brand-rule { height: 1px; background: var(--soft-rule); margin: 12px 0 9px; }
  .card-back .tagline { font-size: 12px; }
  .divider {
    position: absolute; left: 256px; top: 40px; width: 1px; height: 196px;
    background: var(--soft-rule);
  }
  .contact-block { position: absolute; left: 272px; top: 38px; width: 234px; }
  .person-name {
    font-family: "Cinzel", Georgia, serif; font-size: 18px; letter-spacing: 1px;
  }
  .person-role { color: var(--brand-blue); font-size: 13px; margin-top: 4px; padding-left: 60px; }
  .contact-rule { height: 1px; background: var(--soft-rule); margin: 14px 0 12px; }
  .contact-list { list-style: none; }
  .contact-list li {
    display: flex; align-items: center; gap: 8px;
    font-size: 11.5px; margin-bottom: 10px; white-space: nowrap;
  }
  .contact-list svg { width: 15px; height: 15px; flex: none; }
  .web-band {
    position: absolute; left: 0; right: 0; bottom: 14px; height: 40px;
    background: var(--brand-blue); color: #fff;
    display: flex; align-items: center; justify-content: flex-end;
    padding-right: 22px; font-size: 15px; letter-spacing: .3px;
  }
  .grey-strip {
    position: absolute; left: 0; right: 0; bottom: 0; height: 14px;
    background: var(--strip-grey);
  }
</style>
</head>
<body>
  <section class="card card-front" aria-label="Business card front">
    <div class="rule rule-top"></div>
    <div class="brand">
      <span class="brand-square"></span>
      <span class="brand-name">Harbourline<br>Construction</span>
    </div>
    <p class="tagline">New Homes, Addition &amp; Renovation<br>Domestic &amp; Commercial Builders</p>
    <div class="rule rule-bottom"></div>
  </section>

  <section class="card card-back" aria-label="Business card back">
    <div class="brand-block">
      <div class="brand">
        <span class="brand-square"></span>
        <span class="brand-name">Harbourline<br>Construction</span>
      </div>
      <div class="brand-rule"></div>
      <p class="tagline">New Homes, Addition &amp; Renovation<br>Domestic &amp; Commercial Builders</p>
    </div>
    <div class="divider"></div>
    <div class="contact-block">
      <p class="person-name">Daniel Marsh</p>
      <p class="person-role">Director</p>
      <div class="contact-rule"></div>
      <ul class="contact-list">
        <li>
          <svg viewBox="0 0 16 16" aria-hidden="true"><path d="M2 5c0-2 2-3 6-3s6 1 6 3l-3 1-1-2H6L5 6z" fill="#1b8ac7"/><rect x="3" y="7" width="10" height="7" rx="1" fill="#1b8ac7"/><circle cx="8" cy="10.5" r="1.8" fill="#fff"/></svg>
          9312 4470
        </li>
        <li>
          <svg viewBox="0 0 16 16" aria-hidden="true"><rect x="4" y="1" width="8" height="14" rx="1.5" fill="none" stroke="#1b8ac7" stroke-width="1.5"/><circle cx="8" cy="12.5" r=".9" fill="#1b8ac7"/></svg>
          0412558903 (Daniel)
        </li>
        <li>
          <svg viewBox="0 0 16 16" aria-hidden="true"><rect x="1" y="3" width="14" height="10" fill="#1b8ac7"/><path d="M1 3l7 6 7-6M1 13l5-5M15 13l-5-5" fill="none" stroke="#fff" stroke-width="1"/></svg>
          info@harbourlineconstructco.com.au
        </li>
      </ul>
    </div>
    <div class="web-band">www.harbourlineconstructco.com.au</div>
    <div class="grey-strip"></div>
  </section>
</body>
</html>
```